BOLD & MINIMALIST DESIGN NEEDED

We want a very bold but minimalistic business card design that is impactful and utilizes both sides of the business card. Our current logo is included for your use.

We want bold fonts and good use of negative space. We don't want the logo to overpower the design.

Target Market(s)

Professionals who are building new commercial buildings.

Industry/Entity Type

Construction

Contact Information for Business Card

Name, Title, email, office phone, cell phone, website

Font styles to use
Serif
Sans Serif

Requirements
Must have
• Bold design!

```html
<!DOCTYPE html>
<html lang="en">
<head>
<meta charset="utf-8">
<title>Crestmoor Business Card</title>
<link rel="stylesheet" href="https://fonts.googleapis.com/css2?family=Open+Sans:wght@400;700;800&display=swap">
<style>
  :root {
    --page: #e6e7e2;
    --card: #c3c6ba;
    --green: #8cba51;
    --ink: #111111;
  }
  html, body {
    margin: 0;
    width: 1200px;
    height: 1200px;
    overflow: hidden;
    background: var(--page);
    font-family: "Open Sans", Arial, sans-serif;
  }
  .sheet {
    width: 1200px;
    height: 1200px;
    display: flex;
    flex-direction: column;
    align-items: center;
    justify-content: center;
    gap: 50px;
  }
  .card {
    width: 920px;
    height: 526px;
    display: block;
    box-shadow: 0 10px 30px rgba(0,0,0,0.18);
  }
  .card-bg { fill: var(--card); }
  .band { fill: var(--green); }
  .rule { stroke: var(--ink); stroke-width: 5; fill: none; }
  .brand { font-family: "Open Sans", Arial, sans-serif; font-weight: 800; fill: var(--ink); }
  .brand-mark { fill: var(--green); }
  .holder-name { font-weight: 700; font-size: 46px; fill: var(--ink); }
  .designation { font-weight: 400; font-size: 26px; fill: var(--ink); }
  .name-underline { stroke: var(--green); stroke-width: 3; }
  .divider-dark { stroke: var(--ink); stroke-width: 5; }
  .divider-green { stroke: var(--green); stroke-width: 3; }
  .contact { font-weight: 400; font-size: 26px; fill: var(--ink); }
  .icon { fill: none; stroke: var(--ink); stroke-width: 2.2; }
</style>
</head>
<body>
<main class="sheet">

  <!-- Front: contact side -->
  <svg class="card card-front" viewBox="0 0 1050 600" aria-label="Business card front">
    <rect class="card-bg" width="1050" height="600"/>
    <path class="band" d="M0,148 L455,14 Q490,0 525,0 L590,0 L0,174 Z"/>
    <line class="rule" x1="0" y1="176" x2="592" y2="0"/>
    <path class="band" d="M656,0 L800,0 Q780,50 830,110 L1050,400 L1050,505 Z"/>
    <line class="rule" x1="650" y1="0" x2="1050" y2="520"/>

    <g class="brand-lockup" transform="translate(555,190)">
      <rect class="brand-mark" x="-170" y="-28" width="30" height="30"/>
      <text class="brand" x="-128" y="0" font-size="40">CRESTMOOR</text>
    </g>

    <text class="holder-name" x="95" y="335">Holder Name</text>
    <line class="name-underline" x1="97" y1="350" x2="330" y2="350"/>
    <text class="designation" x="95" y="382">Designation</text>

    <line class="divider-dark" x1="478" y1="255" x2="478" y2="530"/>
    <line class="divider-green" x1="484" y1="300" x2="484" y2="530"/>

    <g class="contact-row" transform="translate(545,345)">
      <circle class="icon" cx="0" cy="0" r="16"/>
      <path class="icon" d="M-7,-8 Q-9,2 -1,8 Q5,12 8,7 L4,3 L1,5 Q-4,1 -3,-4 L-1,-6 Z"/>
      <text class="contact" x="36" y="9">+12 345 67890</text>
    </g>
    <g class="contact-row" transform="translate(545,410)">
      <circle class="icon" cx="0" cy="0" r="16"/>
      <rect class="icon" x="-9" y="-6" width="18" height="12"/>
      <path class="icon" d="M-9,-6 L0,2 L9,-6"/>
      <text class="contact" x="36" y="9">yourmail@mail.domain</text>
    </g>
    <g class="contact-row" transform="translate(545,475)">
      <circle class="icon" cx="0" cy="0" r="16"/>
      <circle class="icon" cx="0" cy="0" r="10"/>
      <ellipse class="icon" cx="0" cy="0" rx="4.5" ry="10"/>
      <line class="icon" x1="-10" y1="0" x2="10" y2="0"/>
      <text class="contact" x="36" y="9">yourwebsite.com</text>
    </g>
  </svg>

  <!-- Back: brand side -->
  <svg class="card card-back" viewBox="0 0 1050 600" aria-label="Business card back">
    <rect class="card-bg" width="1050" height="600"/>
    <path class="band" d="M676,0 L820,0 Q800,50 850,110 L1050,380 L1050,485 Z"/>
    <line class="rule" x1="670" y1="0" x2="1050" y2="500"/>

    <g class="brand-lockup" transform="translate(470,345)">
      <rect class="brand-mark" x="-250" y="-46" width="50" height="50"/>
      <text class="brand" x="-182" y="0" font-size="68">CRESTMOOR</text>
    </g>
  </svg>

</main>
</body>
</html>
```